Letterbox drop flyers for local business

I need a flyer design for my small business located in Canberra ACT called "Bluegum Ridge Garden Care" My company is a landscaping business offering garden design, landscaping services, garden maintenance and horticultural services. I would like to have a flyer I can leave at nurseries and do letterbox drops with that highlight the professional quality of our services and also our brand feel of rural Australia and old fashioned vibe. The flyer should highlight our services and our "free quote" policy. Attached is my business logo.

Industry/Entity Type

Small Business

Font styles to use
Serif
Decorative

Colors
f37122
fcca95
ec1f27
abd036
9bcb3c

Requirements
Must have
• A list of our services and all my contact information as well as our offer for free quotes. Present this flyer and customer receives first hour of gardening free
Nice to have
• I would like the overall feel of the design to be old fashioned. Think old painted advertisments for tolleys soap and brimsons biscuits, or an old studley pick-up truck with the dog in the back, want to highlight our quality but also give my customers a feel for our brand as a whole

```html
<!DOCTYPE html>
<html lang="en">
<head>
<meta charset="utf-8">
<title>Bluegum Ridge Garden Care – Flyers</title>
<link href="https://fonts.googleapis.com/css2?family=Questrial&display=swap" rel="stylesheet">
<style>
  :root {
    --backdrop: #ece6da;
    --frame-black: #1a160d;
    --gold-light: #e2bb52;
    --gold-dark: #c49a36;
    --maroon: #7a1c1c;
    --leaf-green: #2f6a24;
    --list-green: #4c8c3a;
    --tan: #d8b865;
    --panel-dark: #1e1a10;
  }
  * { margin: 0; padding: 0; box-sizing: border-box; }
  html, body {
    width: 1200px; height: 867px; overflow: hidden;
    background: var(--backdrop);
    font-family: "Questrial", "Century Gothic", sans-serif;
  }
  .canvas { position: relative; width: 1200px; height: 867px; }

  .flyer { position: absolute; top: 137px; width: 420px; height: 594px; }
  .flyer--front { left: 165px; background: var(--frame-black); }
  .flyer--back { left: 620px; background: var(--panel-dark); }

  .front-panel {
    position: absolute; left: 13px; top: 13px; right: 13px; bottom: 13px;
    background: linear-gradient(160deg, var(--gold-dark) 0%, var(--gold-light) 45%, var(--gold-dark) 100%);
  }

  .brand-name {
    position: absolute; left: 0; right: 0; top: 80px;
    text-align: center; color: var(--maroon); line-height: 1.05;
  }
  .flyer--back .brand-name { top: 93px; }
  .brand-name__main { display: block; font-size: 50px; }
  .brand-name__sub { display: block; font-size: 38px; margin-top: 14px; }

  .ornament {
    position: absolute; left: 42px; top: 280px; width: 310px; height: 95px;
    background: linear-gradient(180deg, rgba(122,28,28,0.18), rgba(122,28,28,0.08));
    border-radius: 4px;
  }

  .contact { position: absolute; left: 32px; right: 32px; top: 388px; text-align: center; color: var(--maroon); }
  .contact__name { font-size: 23px; letter-spacing: 0.5px; line-height: 28px; }
  .contact__rule { height: 2px; background: var(--leaf-green); opacity: 0.7; }
  .contact__phone { font-size: 50px; line-height: 58px; letter-spacing: 1px; }
  .contact__abn { font-size: 14px; letter-spacing: 6.5px; line-height: 24px; }
  .contact__web { font-size: 17px; line-height: 26px; }

  .services { position: absolute; left: 46px; right: 49px; top: 325px; text-align: center; }
  .services__heading { color: var(--tan); font-size: 22px; line-height: 28px; letter-spacing: 0.5px; }
  .services__list { list-style: none; }
  .services__item {
    color: var(--list-green); font-size: 22px; line-height: 31px; letter-spacing: 0.5px;
  }
  .services__rule { position: relative; height: 2px; background: var(--tan); }
  .services__rule::before, .services__rule::after {
    content: ""; position: absolute; top: -2px; width: 6px; height: 6px;
    border-radius: 50%; background: var(--tan);
  }
  .services__rule::before { left: -3px; }
  .services__rule::after { right: -3px; }

  .offer {
    position: absolute; left: 0; right: 0; top: 492px; text-align: center;
    color: var(--tan); font-size: 37px; line-height: 35px; letter-spacing: 0.5px;
  }
</style>
</head>
<body>
<main class="canvas">

  <section class="flyer flyer--front">
    <div class="front-panel">
      <h1 class="brand-name">
        <span class="brand-name__main">Bluegum Ridge</span>
        <span class="brand-name__sub">Garden Care</span>
      </h1>
      <div class="ornament" role="img" aria-label="Decorative maroon scroll flourish"></div>
      <div class="contact">
        <p class="contact__name">MAREN CASTELLANO</p>
        <div class="contact__rule"></div>
        <p class="contact__phone">0455193842</p>
        <div class="contact__rule"></div>
        <p class="contact__abn">ABN:30 615 274 089</p>
        <p class="contact__web">bluegumridgegardensACT.com.au</p>
      </div>
    </div>
  </section>

  <section class="flyer flyer--back">
    <h2 class="brand-name">
      <span class="brand-name__main">Bluegum Ridge</span>
      <span class="brand-name__sub">Garden Care</span>
    </h2>
    <div class="services">
      <p class="services__heading">SPECIALISING IN</p>
      <div class="services__rule"></div>
      <ul class="services__list">
        <li class="services__item">GARDEN MAINTENANCE</li>
        <li class="services__rule"></li>
        <li class="services__item">HORTICULTURE</li>
        <li class="services__rule"></li>
        <li class="services__item">LANDSCAPING</li>
        <li class="services__rule"></li>
        <li class="services__item">DESIGN</li>
        <li class="services__rule"></li>
      </ul>
    </div>
    <p class="offer">CALL US FOR FOR<br>YOUR FREE QUOTE</p>
  </section>

</main>
</body>
</html>
```